Business Card Design Project

Hi,
This is a simple contest. The logo for the back of the card is deigned. See attached files. The front of the card must have :

Directors Name: Tobias
Mob:
e-mail:
Postal Address:
Web Page Adress:

It may also add words: "Leaders in Construction Project Management Services"

Target Market(s)

Business & Home owners alike

Industry/Entity Type

Business

Requirements
Must have
• See details above and logo attached
Should not have
• Images other than logo

```html
<!DOCTYPE html>
<html lang="en">
<head>
<meta charset="utf-8">
<title>Cornerstone Works Australia – Business Card</title>
<link rel="stylesheet" href="https://fonts.googleapis.com/css2?family=Cinzel:wght@400;700&display=swap">
<style>
  :root {
    --page-bg: #e9ebed;
    --card-white: #ffffff;
    --brand-blue: #1f9ad6;
    --card-blue: #2ba6df;
    --text-white: #ffffff;
    --mark-tint: #cfe6f3;
    --shadow: rgba(20, 40, 60, 0.18);
  }
  * { box-sizing: border-box; margin: 0; padding: 0; }
  html, body {
    width: 1200px;
    height: 1200px;
    overflow: hidden;
    background: var(--page-bg);
    font-family: "Cinzel", "Times New Roman", serif;
  }
  .canvas {
    position: relative;
    width: 1200px;
    height: 1200px;
  }
  .card {
    position: absolute;
    left: 180px;
    width: 840px;
    height: 480px;
    box-shadow: 0 6px 22px var(--shadow);
  }
  /* Front */
  .card-front {
    top: 90px;
    background: var(--card-white);
    color: var(--brand-blue);
  }
  .holder-name {
    position: absolute;
    left: 56px;
    top: 46px;
    font-size: 34px;
    letter-spacing: 1px;
  }
  .holder-title {
    position: absolute;
    left: 58px;
    top: 92px;
    font-size: 14px;
    letter-spacing: 1px;
  }
  .contact-details {
    position: absolute;
    left: 58px;
    top: 160px;
    font-size: 14px;
    line-height: 24px;
    letter-spacing: 0.5px;
    list-style: none;
  }
  .online-details {
    position: absolute;
    left: 58px;
    top: 360px;
    font-size: 14px;
    line-height: 26px;
    letter-spacing: 0.5px;
    list-style: none;
  }
  .front-brand {
    position: absolute;
    right: 48px;
    top: 48px;
    width: 330px;
    display: flex;
    flex-direction: column;
    align-items: flex-end;
  }
  .front-brand .brand-square {
    width: 170px;
    height: 170px;
    background: var(--mark-tint);
    margin-right: 80px;
    margin-bottom: 26px;
  }
  .front-brand .brand-name {
    font-size: 30px;
    font-weight: 700;
    line-height: 34px;
    letter-spacing: 1px;
    text-align: right;
  }
  .front-brand .brand-tagline {
    margin-top: 10px;
    font-size: 10px;
    letter-spacing: 0.4px;
    text-align: right;
  }
  /* Back */
  .card-back {
    top: 630px;
    background: var(--card-blue);
    color: var(--text-white);
  }
  .back-brand {
    position: absolute;
    left: 110px;
    top: 96px;
    display: flex;
    align-items: center;
    gap: 22px;
  }
  .back-brand .brand-square {
    width: 70px;
    height: 70px;
    background: var(--text-white);
  }
  .back-brand .brand-name {
    font-size: 38px;
    font-weight: 700;
    line-height: 42px;
    letter-spacing: 1px;
  }
  .back-tagline {
    position: absolute;
    left: 110px;
    top: 200px;
    font-size: 16px;
    letter-spacing: 0.8px;
  }
  .back-web {
    position: absolute;
    left: 0;
    right: 0;
    bottom: 56px;
    text-align: center;
    font-size: 20px;
    letter-spacing: 1.5px;
  }
</style>
</head>
<body>
<main class="canvas">

  <section class="card card-front" aria-label="Card front">
    <h1 class="holder-name">Tobias</h1>
    <p class="holder-title">Chairman Director</p>
    <ul class="contact-details">
      <li>Mobile: 0400 218 736</li>
      <li>48 Harbour Street</li>
      <li>Australia 2000-2001</li>
    </ul>
    <ul class="online-details">
      <li>hello@cornerstoneworks.com</li>
      <li>www.cornerstoneworksaustralia.com</li>
    </ul>
    <div class="front-brand">
      <div class="brand-square"></div>
      <p class="brand-name">Cornerstone Works<br>Australia</p>
      <p class="brand-tagline">Leaders in Construction Project Management Services</p>
    </div>
  </section>

  <section class="card card-back" aria-label="Card back">
    <div class="back-brand">
      <div class="brand-square"></div>
      <p class="brand-name">Cornerstone Works<br>Australia</p>
    </div>
    <p class="back-tagline">Leaders in Construction Project Management Services</p>
    <p class="back-web">www.cornerstoneworksaustralia.com</p>
  </section>

</main>
</body>
</html>
```